Creative Businesss Card desgin!

Create a business card for our business Gleam window cleaning!
We are open to creative ideas as long as it maintains a professional image.

Target Market(s)

Small Commercial window cleaning clients including car dealerships, strata manager, cafe

Industry/Entity Type

Window Cleaning

Contact Information for Business Card

Daniel Prescott
General Manager
Gleam Window Cleaning

daniel@gleamservices.com.au
pane-care-southbank.com.au
Ph: 1800 GET GLEAM
Mob: 0437 582 061

Colors
fbed22
0392cd

Requirements
Should not have
• Stock window cleaning/ squeegee graphics

```html
<!DOCTYPE html>
<html lang="en">
<head>
<meta charset="utf-8">
<title>Gleam Window Cleaning – Business Card</title>
<link href="https://fonts.googleapis.com/css2?family=Montserrat:wght@700;800&family=Open+Sans:wght@400;600&display=swap" rel="stylesheet">
<style>
  :root {
    --blue: #0392cd;
    --blue-soft: #4fabdb;
    --yellow: #fbed22;
    --white: #ffffff;
    --grey-light: #e2e3e5;
    --grey-dark: #606163;
    --ink: #1e1e1e;
    --backdrop: #ece8e1;
  }
  * { margin: 0; padding: 0; box-sizing: border-box; }
  html, body {
    width: 1200px; height: 960px; overflow: hidden;
    background: var(--backdrop);
  }
  .stage {
    width: 1200px; height: 960px;
    display: flex; flex-direction: column; align-items: center; justify-content: center;
    gap: 56px;
  }
  .card {
    position: relative; width: 700px; height: 400px; overflow: hidden;
    box-shadow: 0 10px 28px rgba(0,0,0,0.18);
  }

  /* Back of card */
  .card-back { background: var(--blue-soft); }
  .card-back .stripe {
    position: absolute; left: 0; right: 0; height: 34px; background: var(--yellow);
  }
  .card-back .stripe.top { top: 0; }
  .card-back .stripe.bottom { bottom: 0; }
  .card-back .brand {
    position: absolute; inset: 0;
    display: flex; flex-direction: column; align-items: center; justify-content: center;
  }

  .brand-name {
    font-family: "Montserrat", Arial, sans-serif; font-weight: 800;
    color: var(--yellow); text-transform: uppercase; line-height: 1;
  }
  .card-back .brand-name.main { font-size: 92px; letter-spacing: 4px; }
  .card-back .brand-name.sub { font-size: 30px; letter-spacing: 2px; margin-top: 10px; }

  /* Front of card */
  .card-front { background: var(--white); }
  .front-brand {
    position: absolute; left: 0; top: 0; width: 300px; height: 318px;
    background: var(--blue);
    display: flex; flex-direction: column; align-items: center; justify-content: center;
  }
  .front-brand .brand-name.main { font-size: 64px; letter-spacing: 3px; }
  .front-brand .brand-name.sub { font-size: 20px; letter-spacing: 1px; margin-top: 8px; }

  .person { position: absolute; left: 330px; top: 52px; }
  .person-name {
    font-family: "Montserrat", Arial, sans-serif; font-size: 30px; font-weight: 700;
    color: var(--ink); letter-spacing: 0.5px; text-transform: uppercase;
  }
  .person-name .surname { color: var(--blue); }
  .person-title {
    font-family: "Open Sans", Arial, sans-serif; font-size: 15px; letter-spacing: 1.5px;
    color: var(--blue); text-transform: uppercase; margin-top: 2px;
  }

  .phones {
    position: absolute; left: 300px; right: 0; top: 192px; height: 72px;
    background: linear-gradient(to bottom, var(--white), var(--grey-light));
    padding: 8px 0 0 24px;
  }
  .links {
    position: absolute; left: 300px; right: 0; top: 264px; height: 54px;
    background: var(--grey-dark);
    padding: 6px 0 0 24px;
  }
  .line {
    display: flex; align-items: center; gap: 12px;
    font-family: "Open Sans", Arial, sans-serif; font-size: 17px; height: 26px;
  }
  .phones .line { color: var(--ink); letter-spacing: 0.5px; }
  .links .line { color: var(--white); font-size: 16px; height: 21px; }
  .icon { width: 18px; height: 18px; flex: none; }

  .address-band {
    position: absolute; left: 0; right: 0; bottom: 0; height: 82px;
    background: var(--yellow);
    display: flex; align-items: center; justify-content: center; gap: 10px;
    font-family: "Open Sans", Arial, sans-serif; font-size: 18px; color: var(--ink);
  }
</style>
</head>
<body>
<main class="stage">

  <section class="card card-back" aria-label="Business card back">
    <div class="stripe top"></div>
    <div class="stripe bottom"></div>
    <div class="brand">
      <span class="brand-name main">Gleam</span>
      <span class="brand-name sub">Window Cleaning</span>
    </div>
  </section>

  <section class="card card-front" aria-label="Business card front">
    <div class="front-brand">
      <span class="brand-name main">Gleam</span>
      <span class="brand-name sub">Window Cleaning</span>
    </div>

    <div class="person">
      <h1 class="person-name">Daniel <span class="surname">Prescott</span></h1>
      <p class="person-title">General Manager</p>
    </div>

    <div class="phones">
      <p class="line">
        <svg class="icon" viewBox="0 0 24 24"><path fill="#1e1e1e" d="M6.6 10.8a15 15 0 0 0 6.6 6.6l2.2-2.2c.3-.3.7-.4 1-.2 1.1.4 2.3.6 3.6.6.6 0 1 .4 1 1V20c0 .6-.4 1-1 1A17 17 0 0 1 3 4c0-.6.4-1 1-1h3.5c.6 0 1 .4 1 1 0 1.3.2 2.5.6 3.6.1.3 0 .7-.2 1z"/></svg>
        1800 GET GLEAM
      </p>
      <p class="line">
        <svg class="icon" viewBox="0 0 24 24"><path fill="#1e1e1e" d="M6.6 10.8a15 15 0 0 0 6.6 6.6l2.2-2.2c.3-.3.7-.4 1-.2 1.1.4 2.3.6 3.6.6.6 0 1 .4 1 1V20c0 .6-.4 1-1 1A17 17 0 0 1 3 4c0-.6.4-1 1-1h3.5c.6 0 1 .4 1 1 0 1.3.2 2.5.6 3.6.1.3 0 .7-.2 1z"/></svg>
        0437 582 061
      </p>
    </div>

    <div class="links">
      <p class="line">
        <svg class="icon" viewBox="0 0 24 24"><rect x="2" y="5" width="20" height="14" fill="#fff"/><path d="M2 5l10 8 10-8" fill="none" stroke="#606163" stroke-width="1.6"/></svg>
        daniel@gleamservices.com.au
      </p>
      <p class="line">
        <svg class="icon" viewBox="0 0 24 24" fill="none" stroke="#fff" stroke-width="1.5"><circle cx="12" cy="12" r="9"/><ellipse cx="12" cy="12" rx="4" ry="9"/><path d="M3 12h18M5 7h14M5 17h14"/></svg>
        pane-care-southbank.com.au
      </p>
    </div>

    <div class="address-band">
      <svg class="icon" viewBox="0 0 24 24"><path fill="#1e1e1e" d="M12 2a7 7 0 0 0-7 7c0 5 7 13 7 13s7-8 7-13a7 7 0 0 0-7-7zm0 9.5A2.5 2.5 0 1 1 12 6.5a2.5 2.5 0 0 1 0 5z"/></svg>
      1208/45 Harbour Rd&nbsp; Southbank VIC 3006
    </div>
  </section>

</main>
</body>
</html>
```